Single Page Digital Brochure

We are a Sydney based finance company. We lend money to developers. Please see attached example of what we are looking to have produced. We just need a design which can be posted on LINKEDIN

Target Market(s)

Property Developers who are borrowing money

Industry/Entity Type

Finance

Requirements
Must have
• Australian relevant imagery.

TEXT TO INCLUDE:

New Offering from Ferngate Lending
Nice to have
• Design and colour scheme based around our logo (attached)

Please include the same text as the attachment

Please make the design based loosely on the attachment. But do not copy the attachement
Should not have
• Remove Text: 'Settle in under four days'

```html
<!DOCTYPE html>
<html lang="en">
<head>
<meta charset="utf-8">
<title>Ferngate Lending – Recent Deal</title>
<link rel="stylesheet" href="https://fonts.googleapis.com/css2?family=Anton&family=Lato:wght@400;700&family=Cinzel:wght@600&display=swap">
<style>
  :root {
    --page-bg: #4a4a45;
    --sky-top: #5e5e5e;
    --sky-haze: #8a8a8a;
    --skyline: #6e6e6e;
    --shore: #585858;
    --water: #4a4a4a;
    --water-deep: #3a3a3a;
    --text-light: #ffffff;
    --text-dark: #1e1e1e;
    --footer-bg: #ffffff;
  }
  * { margin: 0; padding: 0; box-sizing: border-box; }
  html, body {
    width: 1200px; height: 1200px; overflow: hidden;
    background: var(--page-bg);
  }
  .post {
    position: absolute; left: 0; top: 200px;
    width: 1200px; height: 800px;
    overflow: hidden;
  }
  .harbour-photo {
    position: absolute; left: 0; top: 0;
    width: 1200px; height: 737px;
    background:
      radial-gradient(ellipse 520px 260px at 500px 610px, rgba(0,0,0,0.22), rgba(0,0,0,0) 70%),
      linear-gradient(180deg,
        var(--sky-top) 0%,
        var(--sky-haze) 30%,
        var(--skyline) 42%,
        var(--shore) 56%,
        var(--water) 66%,
        var(--water-deep) 100%);
  }
  .brand-name {
    position: absolute; left: 833px; top: 136px;
    font-family: "Cinzel", serif; font-weight: 600;
    font-size: 27px; letter-spacing: 0.5px;
    color: var(--text-light);
  }
  .headline {
    position: absolute; left: 73px; top: 312px;
    font-family: "Anton", sans-serif; font-weight: 400;
    font-size: 84px; line-height: 91px;
    color: var(--text-light);
    letter-spacing: 0.5px;
  }
  .deal-terms {
    position: absolute; left: 470px; top: 290px;
    list-style: none;
    font-family: "Lato", sans-serif; font-weight: 400;
    font-size: 36px; line-height: 45.5px;
    color: var(--text-light);
  }
  .deal-terms .label { font-weight: 700; }
  .deal-terms .gap { margin-top: 7px; }
  .footer-band {
    position: absolute; left: 0; top: 737px;
    width: 1200px; height: 63px;
    background: var(--footer-bg);
    display: flex; align-items: center; justify-content: center;
    font-family: "Lato", sans-serif; font-size: 34px;
    color: var(--text-dark);
  }
</style>
</head>
<body>
  <main class="post">
    <div class="harbour-photo" role="img" aria-label="Black and white photo of Sydney Harbour Bridge arching over the water, with the Sydney city skyline and tower behind it"></div>

    <div class="brand-name">Ferngate Lending</div>

    <h1 class="headline">WE DID<br>Just Last<br>Week</h1>

    <ul class="deal-terms">
      <li><span class="label">Loan Amount :</span> $ 750,000</li>
      <li><span class="label">Rate :</span> 7.79%</li>
      <li><span class="label">Term :</span> 12 months</li>
      <li><span class="label">LVR :</span> 60 %</li>
      <li class="gap"><span class="label">Repayment :</span> Capitalised</li>
      <li><span class="label">Security :</span> 2x Sydney Residential Properties</li>
      <li><span class="label">Purpose :</span> Business Working Capital</li>
    </ul>

    <footer class="footer-band">www.ferngatelending.com</footer>
  </main>
</body>
</html>
```